Mo Zest ZA!

This is for a design on Self-serve cups for Frozen Yogurt. The Logo will be available within 2 days from today. Including the selected log, it is necessary to inncoporate 4 primary strong colours that will complement the logo and be a fun, funky cup design. Remember, the cup design will flow through thousands of self-serve cups and create an impressive brand design. The design must be bright, appealling and surround the recylable cup completely.
Please check www.zestchillparade.example to get some idea of the fun aspect.
Cups will be printed in various sizes. from 16oz, to samplers of 2ozs.
Please check other Mo ZestZA! designs on this project website.

Target Market(s)

Youngsters from 5 years to 30 years.

Requirements
Must have
• 4 striking primary coloured stripes surrounding or flowing through the design for frozen yogurt
• The Catch line: Za! Dip the Chill! must appear below the logo or at the back of cup opposite the logo.
Nice to have
• Colourful, heatlhy, fun options of design
Should not have
• Any imitation of any other froyo cup whatsoever.

```html
<!DOCTYPE html>
<html lang="en">
<head>
<meta charset="utf-8">
<title>Mo Zest ZA! – Cup Wrap Colourways</title>
<link rel="stylesheet" href="https://fonts.googleapis.com/css2?family=Source+Sans+3:wght@400&display=swap">
<style>
  :root {
    --stage: #ececec;
    --tagline-yellow: #f4e23a;
    --tagline-white: #ffffff;
    --tagline-brown: #5a2e22;

    --blue-top: #ffffff; --blue-drip: #0f6db5; --blue-band: #1f3a78; --blue-line: #1f6fc0;
    --grey-top: #4a4a4a; --grey-drip: #000000; --grey-band: #4a4a4a; --grey-line: #000000;
    --cream-top: #f6f0b8; --cream-cap: #5a2e22; --cream-band: #5a2e22;
    --red-top: #5e1212; --red-drip: #e2222a; --red-band: #b51a1f; --red-line: #f07070;
    --sky-top: #66c4da; --sky-drip: #0a1e3c; --sky-band: #1d6fc0; --sky-line: #000000;
    --lime-top: #8cc63f; --lime-drip: #1e3f1a; --lime-band: #8cc63f; --lime-line: #1e3f1a;
  }
  html, body { margin: 0; padding: 0; overflow: hidden; }
  body {
    width: 1200px; height: 1116px; position: relative;
    background: radial-gradient(ellipse at center, #fafafa 0%, var(--stage) 100%);
    font-family: "Source Sans 3", sans-serif;
  }
  .wrap-panel {
    position: absolute; width: 282px; height: 250px;
    border: 1px solid #222; box-sizing: border-box; overflow: hidden;
  }
  .wrap-panel svg { display: block; width: 100%; height: 100%; }
  .tagline { font-family: "Source Sans 3", sans-serif; font-size: 17px; font-weight: 400; }
  .pos-blue  { left: 60px;  top: 68px; }
  .pos-grey  { left: 645px; top: 68px; }
  .pos-cream { left: 60px;  top: 443px; }
  .pos-red   { left: 645px; top: 443px; }
  .pos-sky   { left: 60px;  top: 797px; }
  .pos-lime  { left: 645px; top: 808px; }
</style>
</head>
<body>

<svg width="0" height="0" style="position:absolute" aria-hidden="true">
  <defs>
    <linearGradient id="fruit-tones" x1="0" x2="1">
      <stop offset="0" stop-color="#f5a623"/>
      <stop offset="0.3" stop-color="#e0502a"/>
      <stop offset="0.55" stop-color="#9cc63f"/>
      <stop offset="0.8" stop-color="#e8b62a"/>
      <stop offset="1" stop-color="#7a4a6a"/>
    </linearGradient>
    <linearGradient id="flow-blue" x1="0" y1="0" x2="0" y2="1">
      <stop offset="0.3" stop-color="var(--blue-top)"/><stop offset="0.8" stop-color="var(--blue-drip)"/>
    </linearGradient>
    <linearGradient id="flow-grey" x1="0" y1="0" x2="0" y2="1">
      <stop offset="0.3" stop-color="var(--grey-top)"/><stop offset="0.8" stop-color="var(--grey-drip)"/>
    </linearGradient>
    <linearGradient id="flow-red" x1="0" y1="0" x2="0" y2="1">
      <stop offset="0.3" stop-color="var(--red-top)"/><stop offset="0.8" stop-color="var(--red-drip)"/>
    </linearGradient>
    <linearGradient id="flow-sky" x1="0" y1="0" x2="0" y2="1">
      <stop offset="0.3" stop-color="var(--sky-top)"/><stop offset="0.8" stop-color="var(--sky-drip)"/>
    </linearGradient>
    <linearGradient id="flow-lime" x1="0" y1="0" x2="0" y2="1">
      <stop offset="0.3" stop-color="var(--lime-top)"/><stop offset="0.8" stop-color="var(--lime-drip)"/>
    </linearGradient>
  </defs>
</svg>

<div class="wrap-panel pos-blue">
  <svg viewBox="0 0 282 250">
    <rect width="282" height="152" fill="url(#flow-blue)" role="img" aria-label="Illustration of blue frozen yogurt dripping down from a white top"/>
    <rect y="152" width="282" height="66" fill="url(#fruit-tones)" role="img" aria-label="Illustrated row of fruit: orange, watermelon, kiwi, strawberry, pineapple, berries and chocolate"/>
    <rect y="218" width="282" height="24" fill="var(--blue-band)"/>
    <rect y="242" width="282" height="4" fill="#ffffff"/>
    <rect y="246" width="282" height="4" fill="var(--blue-line)"/>
    <text class="tagline" x="141" y="235" text-anchor="middle" fill="var(--tagline-yellow)">Za! Dip the Chill!</text>
  </svg>
</div>

<div class="wrap-panel pos-grey">
  <svg viewBox="0 0 282 250">
    <rect width="282" height="152" fill="url(#flow-grey)" role="img" aria-label="Illustration of black frozen yogurt dripping down from a grey top"/>
    <rect y="152" width="282" height="66" fill="url(#fruit-tones)" role="img" aria-label="Illustrated row of fruit: orange, watermelon, kiwi, strawberry, pineapple, berries and chocolate"/>
    <rect y="218" width="282" height="24" fill="var(--grey-band)"/>
    <rect y="242" width="282" height="4" fill="#ffffff"/>
    <rect y="246" width="282" height="4" fill="var(--grey-line)"/>
    <text class="tagline" x="141" y="235" text-anchor="middle" fill="var(--tagline-white)">Za! Dip the Chill!</text>
  </svg>
</div>

<div class="wrap-panel pos-cream">
  <svg viewBox="0 0 282 250">
    <rect width="282" height="250" fill="var(--cream-top)"/>
    <rect width="282" height="30" fill="var(--cream-cap)"/>
    <rect y="30" width="282" height="125" fill="var(--cream-top)" role="img" aria-label="Decorative pattern of pastel and chocolate coloured dots"/>
    <rect y="155" width="282" height="62" fill="url(#fruit-tones)" role="img" aria-label="Illustrated row of fruit: orange, watermelon, kiwi, strawberry, pineapple, berries and chocolate"/>
    <text class="tagline" x="141" y="234" text-anchor="middle" fill="var(--tagline-brown)">Za! Dip the Chill!</text>
    <rect y="243" width="282" height="7" fill="var(--cream-band)"/>
  </svg>
</div>

<div class="wrap-panel pos-red">
  <svg viewBox="0 0 282 250">
    <rect width="282" height="152" fill="url(#flow-red)" role="img" aria-label="Illustration of red frozen yogurt rising into a dark maroon top"/>
    <rect y="152" width="282" height="64" fill="url(#fruit-tones)" role="img" aria-label="Illustrated row of fruit: orange, watermelon, kiwi, strawberry, pineapple, berries and chocolate"/>
    <rect y="216" width="282" height="24" fill="var(--red-band)"/>
    <rect y="240" width="282" height="4" fill="var(--red-line)"/>
    <rect y="244" width="282" height="6" fill="var(--red-band)"/>
    <text class="tagline" x="141" y="234" text-anchor="middle" fill="var(--tagline-yellow)">Za! Dip the Chill!</text>
  </svg>
</div>

<div class="wrap-panel pos-sky">
  <svg viewBox="0 0 282 250">
    <rect width="282" height="152" fill="url(#flow-sky)" role="img" aria-label="Illustration of navy frozen yogurt dripping down from a sky blue top"/>
    <rect y="152" width="282" height="64" fill="url(#fruit-tones)" role="img" aria-label="Illustrated row of fruit: orange, watermelon, kiwi, strawberry, pineapple, berries and chocolate"/>
    <rect y="216" width="282" height="24" fill="var(--sky-band)"/>
    <rect y="240" width="282" height="10" fill="var(--sky-line)"/>
    <text class="tagline" x="141" y="234" text-anchor="middle" fill="var(--tagline-white)">Za! Dip the Chill!</text>
  </svg>
</div>

<div class="wrap-panel pos-lime">
  <svg viewBox="0 0 282 250">
    <rect width="282" height="152" fill="url(#flow-lime)" role="img" aria-label="Illustration of dark green frozen yogurt dripping down from a lime top"/>
    <rect y="152" width="282" height="64" fill="url(#fruit-tones)" role="img" aria-label="Illustrated row of fruit: orange, watermelon, kiwi, strawberry, pineapple, berries and chocolate"/>
    <rect y="216" width="282" height="26" fill="var(--lime-band)"/>
    <rect y="242" width="282" height="8" fill="var(--lime-line)"/>
    <text class="tagline" x="141" y="235" text-anchor="middle" fill="var(--tagline-yellow)">Za! Dip the Chill!</text>
  </svg>
</div>

</body>
</html>
```